Nursing Concepts Diagram

We are looking to make a diagram to represent the Conceptual Framework of our nursing program (college). The frame work is based on three parts:

I. Nursing Process

II. Core Concepts
a. Clinical Competence
b. Critical Thinking
c. Moral/Ethical Principles
d. Growth Mindset
e. Caring/Compassion
f. Cultural Competence
g. Effective Communication
h. Life-long Learning

III. Tervane's Hierarchy of Needs

I have attached two sketches to give you a sense of how I think this could work.

Please also consider the following:

-Tervane's Hierarchy of Needs is always represented in the shape of a pyramid so I think the other two components (Nursing Process and Core Concepts) should complement that.

Target Market(s)

Healthcare Professionals, Nursing Educators

Font styles to use
Sans Serif

Colors

Designer to choose colors to be used in the design.

Requirements
Must have
• We would like the diagram to include a legend somewhere on the paper that outlines the parts of each component like demonstrated in the attached table
• All the small parts of the Nursing Process and Tervane's Hierarchy of Needs don't need to be listed out in the diagram because it may look too wordy, but the eight parts that make up the core concepts should all be listed
• The Nursing Process and Tervane's Hierachy of needs should both border each of the 8 core concepts so that it can show a relation.

```html
<!DOCTYPE html>
<html lang="en">
<head>
<meta charset="utf-8">
<title>Nursing Concepts Framework</title>
<link href="https://fonts.googleapis.com/css2?family=Josefin+Sans:wght@400;600;700&family=Poppins:wght@400;600&display=swap" rel="stylesheet">
<style>
  :root {
    --bg: #ffffff;
    --frame-blue: #04a9e9;
    --core-yellow: #f4c300;
    --title-brown: #4a3b12;
    --heading-orange: #f2560f;
    --legend-text: #3a3a3a;
    --label-white: #ffffff;
  }
  html, body {
    margin: 0;
    padding: 0;
    width: 1200px;
    height: 927px;
    overflow: hidden;
    background: var(--bg);
  }
  .framework {
    position: relative;
    width: 1200px;
    height: 927px;
  }
  .framework-diagram {
    position: absolute;
    inset: 0;
  }
  .legend {
    position: absolute;
    font-family: "Poppins", sans-serif;
  }
  .legend--left { left: 30px; top: 76px; }
  .legend--right { left: 813px; top: 76px; }
  .legend-group + .legend-group { margin-top: 18px; }
  .legend-heading {
    margin: 0 0 11px;
    color: var(--heading-orange);
    font-size: 19px;
    font-weight: 600;
    line-height: 26px;
  }
  .legend-list {
    list-style: none;
    margin: 0;
    padding: 0;
  }
  .legend-item {
    position: relative;
    padding-left: 18px;
    color: var(--legend-text);
    font-size: 14.5px;
    line-height: 27.2px;
  }
  .legend-item::before {
    content: "";
    position: absolute;
    left: 0;
    top: 9px;
    width: 7px;
    height: 7px;
    border: 1.5px solid var(--legend-text);
    border-radius: 50%;
    background: radial-gradient(circle, var(--legend-text) 0 1.6px, transparent 2px);
  }
  .band-label {
    font-family: "Josefin Sans", sans-serif;
    font-weight: 600;
    fill: var(--label-white);
    letter-spacing: 1px;
  }
  .frame-label {
    font-family: "Josefin Sans", sans-serif;
    font-weight: 700;
    fill: var(--label-white);
    font-size: 48px;
    letter-spacing: 9px;
  }
  .core-title {
    font-family: "Josefin Sans", sans-serif;
    font-weight: 600;
    fill: var(--title-brown);
  }
</style>
</head>
<body>
<main class="framework">
  <svg class="framework-diagram" width="1200" height="927" viewBox="0 0 1200 927" role="img" aria-label="Nursing concepts pyramid: the nursing process frames eight core concepts around Tervane's Hierarchy of Needs">
    <defs>
      <linearGradient id="grad-growth" x1="1" y1="0" x2="0" y2="1"><stop offset="0" stop-color="#19c9c6"/><stop offset="1" stop-color="#0b6f72"/></linearGradient>
      <linearGradient id="grad-lifelong" x1="0" y1="0" x2="1" y2="1"><stop offset="0" stop-color="#b400b4"/><stop offset="1" stop-color="#560062"/></linearGradient>
      <linearGradient id="grad-caring" x1="1" y1="0" x2="0" y2="1"><stop offset="0" stop-color="#ff6e5e"/><stop offset="1" stop-color="#ff1f1f"/></linearGradient>
      <linearGradient id="grad-clinical" x1="0" y1="0" x2="1" y2="1"><stop offset="0" stop-color="#7e4234"/><stop offset="1" stop-color="#2a1618"/></linearGradient>
      <linearGradient id="grad-cultural" x1="1" y1="0" x2="0" y2="1"><stop offset="0" stop-color="#8286f2"/><stop offset="1" stop-color="#3423cc"/></linearGradient>
      <linearGradient id="grad-critical" x1="0" y1="0" x2="1" y2="1"><stop offset="0" stop-color="#bfe43a"/><stop offset="1" stop-color="#5fab1c"/></linearGradient>
      <linearGradient id="grad-communication" x1="0" y1="0" x2="1" y2="0"><stop offset="0" stop-color="#068a3a"/><stop offset="1" stop-color="#13d4b4"/></linearGradient>
      <linearGradient id="grad-ethics" x1="0" y1="0" x2="1" y2="0"><stop offset="0" stop-color="#ff5cbc"/><stop offset="1" stop-color="#ff2452"/></linearGradient>
    </defs>

    <polygon class="process-frame" points="601,52 1148,912 68,912" fill="var(--frame-blue)"/>

    <g class="core-concepts">
      <polygon class="concept concept--growth" points="602,137 602,297 550,385 456,385" fill="url(#grad-growth)"/>
      <polygon class="concept concept--lifelong" points="602,137 748,385 655,385 602,297" fill="url(#grad-lifelong)"/>
      <polygon class="concept concept--caring" points="456,385 550,385 407,625 314,625" fill="url(#grad-caring)"/>
      <polygon class="concept concept--clinical" points="748,385 889,625 799,625 655,385" fill="url(#grad-clinical)"/>
      <polygon class="concept concept--cultural" points="314,625 407,625 323,767 183,847" fill="url(#grad-cultural)"/>
      <polygon class="concept concept--critical" points="889,625 1020,847 885,767 799,625" fill="url(#grad-critical)"/>
      <polygon class="concept concept--communication" points="183,847 323,767 602,767 602,847" fill="url(#grad-communication)"/>
      <polygon class="concept concept--ethics" points="602,767 885,767 1020,847 602,847" fill="url(#grad-ethics)"/>
    </g>

    <polygon class="needs-core" points="602,297 885,767 323,767" fill="var(--core-yellow)"/>

    <text class="frame-label" transform="translate(384,484) rotate(-59.5)" text-anchor="middle">NURSING</text>
    <text class="frame-label" transform="translate(795,440) rotate(59.5)" text-anchor="middle">PROCESS</text>

    <g class="band-label" font-size="21" text-anchor="middle">
      <text transform="translate(535,312) rotate(-59.5)"><tspan x="0" y="-6">GROWTH</tspan><tspan x="0" y="18">MINDSET</tspan></text>
      <text transform="translate(668,308) rotate(59.5)"><tspan x="0" y="-6">LIFE-LONG</tspan><tspan x="0" y="18">LEARNING</tspan></text>
      <text transform="translate(443,499) rotate(-59.5)"><tspan x="0" y="-6">CARING/</tspan><tspan x="0" y="18">COMPASSION</tspan></text>
      <text transform="translate(762,499) rotate(59.5)"><tspan x="0" y="-6">CLINICAL</tspan><tspan x="0" y="18">COMPETENCE</tspan></text>
      <text transform="translate(323,701) rotate(-59.5)"><tspan x="0" y="-6">CULTURAL</tspan><tspan x="0" y="18">COMPETENCE</tspan></text>
      <text transform="translate(874,690) rotate(59.5)"><tspan x="0" y="-6">CRITICAL</tspan><tspan x="0" y="18">THINKING</tspan></text>
      <text x="432" y="804">EFFECTIVE</text>
      <text x="432" y="832" textLength="216" lengthAdjust="spacing">COMMUNICATION</text>
      <text x="768" y="804">MORAL/</text>
      <text x="770" y="832">ETHICAL PRINCIPLES</text>
    </g>

    <g class="core-title" text-anchor="middle">
      <text x="600" y="625" font-size="48" textLength="284" lengthAdjust="spacing">TERVANE'S</text>
      <text x="601" y="688" font-size="48" textLength="392" lengthAdjust="spacing">HIERARCHY</text>
      <text x="601" y="750" font-size="48" textLength="392" lengthAdjust="spacing">OF NEEDS</text>
    </g>
  </svg>

  <aside class="legend legend--left">
    <section class="legend-group">
      <h2 class="legend-heading">Nursing Process</h2>
      <ul class="legend-list">
        <li class="legend-item">Assessment</li>
        <li class="legend-item">Nursing Diagnosis</li>
        <li class="legend-item">Planning</li>
        <li class="legend-item">Intervention</li>
        <li class="legend-item">Evaluation</li>
      </ul>
    </section>
    <section class="legend-group">
      <h2 class="legend-heading">Core Concepts</h2>
      <ul class="legend-list">
        <li class="legend-item">Clinical Competence</li>
        <li class="legend-item">Critical Thinking</li>
        <li class="legend-item">Moral/Ethical Principles</li>
        <li class="legend-item">Growth Mindset</li>
        <li class="legend-item">Caring/Compassion</li>
        <li class="legend-item">Cultural Competence</li>
        <li class="legend-item">Effective Communication</li>
        <li class="legend-item">Life-long Learning</li>
      </ul>
    </section>
  </aside>

  <aside class="legend legend--right">
    <section class="legend-group">
      <h2 class="legend-heading">Tervane's Hierarchy of Needs</h2>
      <ul class="legend-list">
        <li class="legend-item">Self-actualization</li>
        <li class="legend-item">Esteem</li>
        <li class="legend-item">Love and Belonging</li>
        <li class="legend-item">Safety Needs</li>
        <li class="legend-item">Physiological Needs</li>
      </ul>
    </section>
  </aside>
</main>
</body>
</html>
```